Veteran Owned General Contractor needs Bold New Business Cards

We are a service disabled veteran owned small business. We're a general contractor that specializes in excavation, underground utilities, site work, land clearing and demolition. We would like a fresh, simple, bold, new look for our business cards. We're open to ideas! We'd like to incorporate the following information on the card:

Company Name & Logo, Name of Person, Job Title, Office Phone, Fax, Cell Phone, Email Address, Website, SDVOSB

Our logo is included. We look forward to your thoughts.

Thank you!
Updates

Reason: Hello Due to the overwhelming response to this project, we are extending the deadline one time to allow for improved communication and feedback with the top candidates. We would like to thank everyone for their hard work and exceptional creativity! Thank you

Industry/Entity Type

Business

Contact Information for Business Card

Font styles to use
Sans Serif

Requirements
Nice to have
• As we are a veteran owned company, it would be nice to incorporate an American flag into the design. Maybe on the back?

```html
<!DOCTYPE html>
<html lang="en">
<head>
<meta charset="utf-8">
<title>Stonefield Inc — Business Cards</title>
<link href="https://fonts.googleapis.com/css2?family=Open+Sans:wght@400;800&display=swap" rel="stylesheet">
<style>
  :root {
    --backdrop: #3b3330;
    --card: #111111;
    --card-edge: #1c1c1c;
    --brand-green: #5cc33b;
    --text-light: #e9e9e9;
    --divider: #3a3a3a;
    --icon-green: #5cc33b;
  }
  * { margin: 0; padding: 0; box-sizing: border-box; }
  html, body {
    width: 1200px;
    height: 844px;
    overflow: hidden;
  }
  body {
    background: var(--backdrop);
    font-family: "Open Sans", Arial, sans-serif;
    position: relative;
  }
  .card {
    position: absolute;
    top: 272px;
    width: 525px;
    height: 300px;
    background: var(--card);
    border: 1px solid var(--card-edge);
    box-shadow: 0 12px 30px rgba(0,0,0,0.45);
  }
  .card--front { left: 50px; }
  .card--back { left: 625px; }

  .brand {
    display: flex;
    align-items: center;
    gap: 12px;
  }
  .brand__mark {
    width: 40px;
    height: 40px;
    background: var(--brand-green);
    border-radius: 6px;
  }
  .brand__name {
    font-weight: 800;
    font-size: 40px;
    letter-spacing: 2px;
    color: var(--brand-green);
    text-transform: uppercase;
    line-height: 1;
  }

  .card--front .brand {
    position: absolute;
    left: 70px;
    top: 58px;
  }
  .card--back .brand {
    position: absolute;
    left: 50%;
    top: 50%;
    transform: translate(-50%, -50%);
  }

  .person {
    position: absolute;
    right: 283px;
    top: 150px;
    text-align: right;
    color: var(--text-light);
  }
  .person__name {
    font-size: 21px;
    color: var(--brand-green);
    line-height: 1.1;
  }
  .person__title {
    font-size: 14px;
    margin-top: 2px;
  }
  .person__address {
    font-size: 14px;
    line-height: 1.3;
    margin-top: 18px;
  }

  .divider {
    position: absolute;
    left: 258px;
    top: 145px;
    width: 1px;
    height: 112px;
    background: var(--divider);
  }

  .contacts {
    position: absolute;
    left: 275px;
    top: 150px;
    list-style: none;
    color: var(--text-light);
    font-size: 14px;
  }
  .contacts__item {
    display: flex;
    align-items: center;
    gap: 10px;
    height: 22px;
  }
  .contacts__icon {
    width: 11px;
    height: 11px;
    fill: var(--icon-green);
    flex: none;
  }
</style>
</head>
<body>
  <section class="card card--front" aria-label="Business card front">
    <div class="brand">
      <span class="brand__mark"></span>
      <span class="brand__name">Stonefield Inc</span>
    </div>

    <div class="person">
      <p class="person__name">Marcus Hale</p>
      <p class="person__title">Managing Director</p>
      <p class="person__address">12345, Address Goes Here<br>Country Name, 123456</p>
    </div>

    <div class="divider"></div>

    <ul class="contacts">
      <li class="contacts__item">
        <svg class="contacts__icon" viewBox="0 0 12 12" aria-hidden="true"><path d="M2.5 0.5l2 2.5-1.2 1.2c.7 1.6 1.9 2.8 3.5 3.5L8 6.5l2.5 2-1 2.5C4.8 10.6 1.4 7.2 0 2.5z"/></svg>
        <span>(044)-456-7890</span>
      </li>
      <li class="contacts__item">
        <svg class="contacts__icon" viewBox="0 0 12 12" aria-hidden="true"><path d="M3 0h6v3H3zM0 4h12v5h-2v3H2V9H0zM3 7v4h6V7z"/></svg>
        <span>123-456-7890</span>
      </li>
      <li class="contacts__item">
        <svg class="contacts__icon" viewBox="0 0 12 12" aria-hidden="true"><path d="M0 2h12v1L6 7 0 3zM0 4.2l6 4 6-4V10H0z"/></svg>
        <span>info@youremail.com</span>
      </li>
      <li class="contacts__item">
        <svg class="contacts__icon" viewBox="0 0 12 12" aria-hidden="true"><circle cx="6" cy="6" r="6"/></svg>
        <span>www.website.com</span>
      </li>
    </ul>
  </section>

  <section class="card card--back" aria-label="Business card back">
    <div class="brand">
      <span class="brand__mark"></span>
      <span class="brand__name">Stonefield Inc</span>
    </div>
  </section>
</body>
</html>
```